Designing a website for Korvale Pest Solutions PTY LTD

Pest control company looking for someone to build an informative website containing services we offer and an online inquiry form.
Commercial premises - Specialising in - Rodent control, stored product pest control, flying insect control, ant, spider and insect control, Termite inspections and treatments. Termite management systems on a commercial scale.
Facilities we service
Commercial - shopping centres, transport facilities, restaurants, pubs, clubs, bars food manufacturing facilities.
Residential - Houses specialising in - Rodent, Ant, Spider, Cockroach and Termite control. Termite inspections, Pre - purchase inspections, Termite treatments, Termite management systems.
Target Market(s)
Mainly commercial and industrial clients and Residential clients.
Industry/Entity Type
Pest Control
Number of Pages Required
1 page
Look and feel
Each slider illustrates characteristics of the customer's brand and the style your logo design should communicate.

```html
<!DOCTYPE html>
<html lang="en">
<head>
<meta charset="utf-8">
<title>Korvale Pest Solutions PTY LTD</title>
<link href="https://fonts.googleapis.com/css2?family=Outfit:wght@300;400;500;600;700;800&family=Lora:ital@1&display=swap" rel="stylesheet">
<style>
:root{
  --green:#3f9a1c;
  --green-bright:#55b52b;
  --green-dark:#2c7a10;
  --green-pale:#e6f4dd;
  --ink:#1d1d1d;
  --text:#555;
  --muted:#8a8a8a;
  --line:#d9d9d9;
  --panel:#f7f8f7;
  --footer:#1d2124;
  --white:#fff;
  --star:#f0a51b;
}
*{box-sizing:border-box;margin:0;padding:0}
html,body{width:1200px;height:4422px;overflow:hidden}
body{font-family:"Outfit",sans-serif;color:var(--ink);background:var(--white);position:relative}
.page{position:relative;width:1200px;height:4422px;overflow:hidden}
.abs{position:absolute}
.btn{position:absolute;display:flex;align-items:center;justify-content:center;background:var(--green);color:var(--white);border-radius:30px;font-size:13px;font-weight:500;text-decoration:none}

/* header */
.header{position:absolute;left:0;top:0;width:1200px;height:77px;background:var(--white);z-index:3;box-shadow:0 1px 6px rgba(0,0,0,.06)}
.brand{position:absolute;left:163px;top:24px;display:flex;align-items:center;gap:8px;font-size:26px;font-weight:700;color:var(--ink)}
.brand-dot{width:14px;height:14px;border-radius:50%;background:var(--green)}
.nav{position:absolute;top:30px;font-size:13px;color:#555}
.nav.active{color:var(--green);font-weight:600}
.nav.active::after{content:"";position:absolute;left:-4px;right:-4px;bottom:-6px;height:6px;border-bottom:2px solid var(--green);border-radius:0 0 50% 50%}

/* hero */
.hero-photo{position:absolute;left:0;top:77px;width:1200px;height:690px;background:linear-gradient(100deg,#d8dcdf 0%,#9aa3a8 18%,#3a4247 38%,#222a2e 60%,#1a2024 100%)}
.hero-wave{position:absolute;left:0;top:580px;width:1200px;height:200px}
.hero-kicker{left:630px;top:268px;color:var(--white);font-size:16px}
.hero-title{left:628px;top:300px;color:var(--white);font-size:46px;line-height:54px;font-weight:400}
.hero-title b{color:var(--green-bright);font-weight:800}
.hero-arrow{position:absolute;width:50px;height:50px;border-radius:50%;display:flex;align-items:center;justify-content:center}
.dots{position:absolute;display:flex;gap:8px}
.dots i{width:10px;height:10px;border-radius:50%;border:1.5px solid var(--white);display:block}
.dots i.on{background:var(--green-bright);border-color:var(--green-bright)}

/* welcome */
.eyebrow{font-size:19px;color:var(--ink)}
.section-title{font-size:33px;font-weight:700;color:var(--green)}
.para{font-size:12.5px;line-height:22px;color:var(--text)}
.ticks{list-style:none;font-size:12.5px;color:#333}
.ticks li{display:flex;align-items:center;gap:10px;height:27px}
.tick{width:14px;height:14px;flex:none}

/* services */
.services-bg{position:absolute;left:0;top:1320px;width:1200px;height:740px}
.card{position:absolute;width:163px;height:163px;background:var(--white);box-shadow:0 2px 14px rgba(0,0,0,.06);display:flex;flex-direction:column;align-items:center;justify-content:flex-end;padding-bottom:22px;font-size:13.5px;line-height:16px;text-align:center;color:#333}
.card.on{background:var(--green);color:var(--white)}
.card .ic{width:56px;height:56px;margin-bottom:16px}

/* feature */
.photo{position:absolute;border-radius:6px;box-shadow:0 10px 30px rgba(0,0,0,.18)}
.badge{position:absolute;width:64px;height:64px;border-radius:50%;background:#161616;display:flex;align-items:center;justify-content:center}

/* testimonials */
.tcard{position:absolute;width:335px;height:190px;background:var(--white);border-radius:14px;text-align:center;padding:60px 26px 0}
.tcard p{font-family:"Lora",serif;font-style:italic;font-size:12px;line-height:18px;color:#666}
.quote{position:absolute;left:0;right:0;top:12px;text-align:center;font-size:60px;line-height:60px;color:#d7d7d7;font-family:"Lora",serif}
.stars{color:var(--star);font-size:13px;letter-spacing:2px;margin-top:8px}
.tail{position:absolute;width:0;height:0}
.avatar{position:absolute;width:76px;height:76px;border-radius:50%;border:4px solid var(--white);background:radial-gradient(circle at 50% 40%,#c9a58c,#6d5444)}
.who{position:absolute;color:var(--white);font-size:9.5px;font-weight:700;line-height:16px;letter-spacing:.3px}

/* contact */
.contact-card{position:absolute;left:319px;top:3649px;width:562px;height:352px;background:var(--white);border:1px solid #e3e3e3;border-radius:8px;box-shadow:0 6px 26px rgba(0,0,0,.08)}
.field{position:absolute;border-bottom:1px solid var(--line);height:46px}
.field label{display:block;font-size:8.5px;font-weight:600;color:#222;text-transform:uppercase}
.field span{display:block;font-size:9.5px;color:var(--muted);margin-top:10px}

/* footer */
.footer{position:absolute;left:0;top:4100px;width:1200px;height:322px;background:var(--footer)}
.fhead{position:absolute;color:var(--white);font-size:12.5px;font-weight:500;text-transform:uppercase}
.flink{position:absolute;color:#c9cdcf;font-size:11px;line-height:21px}
.social{position:absolute;width:26px;height:26px;border:1px solid #c9cdcf;border-radius:50%}
.copy{position:absolute;font-size:10px;color:#bfc3c5}
</style>
</head>
<body>
<div class="page">

<!-- header -->
<header class="header">
  <div class="brand"><span class="brand-dot"></span>Korvale</div>
  <span class="nav active" style="left:429px">Home</span>
  <span class="nav" style="left:494px">About Us</span>
  <span class="nav" style="left:579px">Services</span>
  <span class="nav" style="left:659px">Pricing</span>
  <span class="nav" style="left:731px">Blog</span>
  <span class="nav" style="left:783px">Contact</span>
  <a class="btn" style="left:867px;top:21px;width:171px;height:35px;font-size:13.5px">Request An Estimate</a>
</header>

<!-- hero -->
<div class="hero-photo" role="img" aria-label="Technician in white protective suit spraying pesticide in a dark gym"></div>
<svg class="hero-wave" viewBox="0 0 1200 200" preserveAspectRatio="none" aria-hidden="true">
  <path d="M0 60 C300 160 700 200 1200 80 L1200 200 L0 200Z" fill="var(--green)"/>
  <path d="M0 70 C300 160 700 180 1200 95 L1200 200 L0 200Z" fill="var(--white)"/>
</svg>
<div class="abs hero-kicker">Pest Control</div>
<div class="abs hero-title">AN EXPERT<br><b>PEST SERVICE</b><br>YOU CAN <b>TRUST</b></div>
<a class="btn" style="left:635px;top:484px;width:158px;height:41px;background:var(--green-bright);font-size:12.5px;font-weight:600">OUR SERVICES</a>
<div class="hero-arrow" style="left:47px;top:306px;border:1.5px solid var(--green)">
  <svg width="14" height="14" viewBox="0 0 14 14"><path d="M9 2 L4 7 L9 12" stroke="var(--green-bright)" stroke-width="2" fill="none"/></svg>
</div>
<div class="hero-arrow" style="left:1103px;top:306px;background:var(--green)">
  <svg width="14" height="14" viewBox="0 0 14 14"><path d="M5 2 L10 7 L5 12" stroke="var(--white)" stroke-width="2" fill="none"/></svg>
</div>
<div class="dots" style="left:566px;top:671px"><i></i><i class="on"></i><i></i><i></i></div>

<!-- welcome -->
<div class="abs eyebrow" style="left:208px;top:872px">Welcome To our</div>
<div class="abs section-title" style="left:208px;top:900px">Korvale Pest Solutions</div>
<p class="abs para" style="left:208px;top:956px;width:390px">Lorem ipsum dolor sit amet, consectetur adipiscing elit. Praesent tincidunt augue et sem feugiat, at fermentum orci laoreet. Duis iaculis sit amet mauris et auctor.</p>
<ul class="abs ticks" style="left:208px;top:1036px">
  <li><svg class="tick" viewBox="0 0 14 14"><circle cx="7" cy="7" r="6" stroke="var(--green)" fill="none"/><path d="M4 7 L6.2 9.2 L10 5" stroke="var(--green)" fill="none" stroke-width="1.4"/></svg>Quality Control System, 100% Satisfaction Guarantee.</li>
  <li><svg class="tick" viewBox="0 0 14 14"><circle cx="7" cy="7" r="6" stroke="var(--green)" fill="none"/><path d="M4 7 L6.2 9.2 L10 5" stroke="var(--green)" fill="none" stroke-width="1.4"/></svg>Highly Professional Staff, Accurate Testing Processes.</li>
  <li><svg class="tick" viewBox="0 0 14 14"><circle cx="7" cy="7" r="6" stroke="var(--green)" fill="none"/><path d="M4 7 L6.2 9.2 L10 5" stroke="var(--green)" fill="none" stroke-width="1.4"/></svg>Unrivalled workmanship, professionaland Qualified.</li>
</ul>
<a class="btn" style="left:209px;top:1140px;width:112px;height:33px">Learn More</a>
<div class="abs" role="img" aria-label="Technician treating a wooden wardrobe for pests" style="left:655px;top:890px;width:390px;height:270px;border-radius:50%;transform:rotate(-18deg);background:linear-gradient(135deg,#6b2f12,#b86a3a 45%,#3a5e8a 70%,#c2263d)"></div>

<!-- services -->
<svg class="services-bg" viewBox="0 0 1200 740" preserveAspectRatio="none" aria-hidden="true">
  <path d="M0 60 C200 0 380 80 620 60 C820 40 960 0 1200 70 L1200 640 C900 720 400 700 0 730Z" fill="var(--panel)"/>
</svg>
<div class="abs" style="left:0;width:1200px;top:1415px;text-align:center;font-size:14.5px;color:#333">Specialising in</div>
<div class="abs" style="left:0;width:1200px;top:1442px;text-align:center;font-size:38px;font-weight:300">Our <b style="color:var(--green);font-weight:700">Services</b></div>

<div class="card on" style="left:246px;top:1537px"><svg class="ic" viewBox="0 0 56 56" role="img" aria-label="Cockroach icon"><circle cx="28" cy="28" r="18" fill="none" stroke="var(--white)" stroke-width="2"/></svg>Pest<br>Control</div>
<div class="card" style="left:428px;top:1537px"><svg class="ic" viewBox="0 0 56 56" role="img" aria-label="Rodent icon"><circle cx="28" cy="28" r="18" fill="none" stroke="var(--green)" stroke-width="2"/></svg>Rodent<br>Control</div>
<div class="card" style="left:610px;top:1537px"><svg class="ic" viewBox="0 0 56 56" role="img" aria-label="Stored product pest icon"><circle cx="28" cy="28" r="18" fill="none" stroke="var(--green)" stroke-width="2"/></svg>Stored Product<br>Pest Control</div>
<div class="card" style="left:792px;top:1537px"><svg class="ic" viewBox="0 0 56 56" role="img" aria-label="Flying insect icon"><circle cx="28" cy="28" r="18" fill="none" stroke="var(--green)" stroke-width="2"/></svg>Flying Insect<br>Control</div>
<div class="card" style="left:337px;top:1719px"><svg class="ic" viewBox="0 0 56 56" role="img" aria-label="Ant icon"><circle cx="28" cy="28" r="18" fill="none" stroke="var(--green)" stroke-width="2"/></svg>Ant<br>Control</div>
<div class="card" style="left:519px;top:1719px"><svg class="ic" viewBox="0 0 56 56" role="img" aria-label="Spider web icon"><circle cx="28" cy="28" r="18" fill="none" stroke="var(--green)" stroke-width="2"/></svg>Spider &amp; Insect<br>Control</div>
<div class="card" style="left:701px;top:1719px"><svg class="ic" viewBox="0 0 56 56" role="img" aria-label="Termite inspection icon"><circle cx="28" cy="28" r="18" fill="none" stroke="var(--green)" stroke-width="2"/></svg>Termite Inspections<br>&amp; Treatments</div>
<div class="abs" role="img" aria-label="Technician in protective suit with sprayer" style="left:995px;top:1530px;width:205px;height:385px;border-radius:60px 0 0 30px;background:linear-gradient(180deg,#d9dde1,#9fa6ad 60%,#c9d34a 80%,#8e9398)"></div>

<!-- commercial -->
<div class="photo" role="img" aria-label="Smiling pest technician with sprayer giving thumbs up" style="left:196px;top:2124px;width:391px;height:324px;background:linear-gradient(120deg,#e8edf0,#b9c4cc 40%,#3b5d8a 70%,#e2d4c7)"></div>
<div class="badge" style="left:555px;top:2255px" aria-hidden="true">
  <svg width="20" height="26" viewBox="0 0 20 26"><path d="M2 1h16v24H2z M5 5h3v3H5z M12 5h3v3h-3z M5 11h3v3H5z M12 11h3v3h-3z M5 17h3v3H5z M12 17h3v3h-3z" fill="var(--white)" fill-rule="evenodd"/></svg>
</div>
<div class="abs section-title" style="left:666px;top:2145px;font-size:25px">Commercial</div>
<p class="abs para" style="left:666px;top:2188px;width:320px;font-size:12px;line-height:19px">Lorem ipsum dolor sit amet, consectetur elit. Aliquam ante enim, tempus vitae nulla eu, luctus maximus enim. Curabitur pretium, tortor et bibendum tempus, turpis augue blandit nulla.</p>
<ul class="abs ticks" style="left:666px;top:2284px">
  <li><svg class="tick" viewBox="0 0 14 14"><circle cx="7" cy="7" r="6" stroke="var(--green)" fill="none"/><path d="M4 7 L6.2 9.2 L10 5" stroke="var(--green)" fill="none" stroke-width="1.4"/></svg>Shopping Centres</li>
  <li><svg class="tick" viewBox="0 0 14 14"><circle cx="7" cy="7" r="6" stroke="var(--green)" fill="none"/><path d="M4 7 L6.2 9.2 L10 5" stroke="var(--green)" fill="none" stroke-width="1.4"/></svg>Transport Facilities</li>
  <li><svg class="tick" viewBox="0 0 14 14"><circle cx="7" cy="7" r="6" stroke="var(--green)" fill="none"/><path d="M4 7 L6.2 9.2 L10 5" stroke="var(--green)" fill="none" stroke-width="1.4"/></svg>Restaurants</li>
</ul>
<ul class="abs ticks" style="left:853px;top:2284px">
  <li><svg class="tick" viewBox="0 0 14 14"><circle cx="7" cy="7" r="6" stroke="var(--green)" fill="none"/><path d="M4 7 L6.2 9.2 L10 5" stroke="var(--green)" fill="none" stroke-width="1.4"/></svg>Pubs</li>
  <li><svg class="tick" viewBox="0 0 14 14"><circle cx="7" cy="7" r="6" stroke="var(--green)" fill="none"/><path d="M4 7 L6.2 9.2 L10 5" stroke="var(--green)" fill="none" stroke-width="1.4"/></svg>Clubs</li>
  <li><svg class="tick" viewBox="0 0 14 14"><circle cx="7" cy="7" r="6" stroke="var(--green)" fill="none"/><path d="M4 7 L6.2 9.2 L10 5" stroke="var(--green)" fill="none" stroke-width="1.4"/></svg>Bars &amp; Manufacturing</li>
</ul>
<a class="btn" style="left:668px;top:2387px;width:112px;height:31px">Learn More</a>

<!-- residential -->
<div class="abs" style="left:0;top:2524px;width:1200px;height:520px;background:var(--panel)"></div>
<div class="abs section-title" style="left:197px;top:2658px;font-size:25px">Residential</div>
<p class="abs para" style="left:197px;top:2700px;width:320px;font-size:12px;line-height:19px">Lorem ipsum dolor sit amet, consectetur elit. Aliquam ante enim, tempus vitae nulla eu, luctus maximus enim. Curabitur pretium, tortor et bibendum tempus, turpis augue blandit nulla.</p>
<ul class="abs ticks" style="left:197px;top:2798px">
  <li><svg class="tick" viewBox="0 0 14 14"><circle cx="7" cy="7" r="6" stroke="var(--green)" fill="none"/><path d="M4 7 L6.2 9.2 L10 5" stroke="var(--green)" fill="none" stroke-width="1.4"/></svg>Houses Specialising</li>
  <li><svg class="tick" viewBox="0 0 14 14"><circle cx="7" cy="7" r="6" stroke="var(--green)" fill="none"/><path d="M4 7 L6.2 9.2 L10 5" stroke="var(--green)" fill="none" stroke-width="1.4"/></svg>Rodent</li>
  <li><svg class="tick" viewBox="0 0 14 14"><circle cx="7" cy="7" r="6" stroke="var(--green)" fill="none"/><path d="M4 7 L6.2 9.2 L10 5" stroke="var(--green)" fill="none" stroke-width="1.4"/></svg>Ant</li>
  <li><svg class="tick" viewBox="0 0 14 14"><circle cx="7" cy="7" r="6" stroke="var(--green)" fill="none"/><path d="M4 7 L6.2 9.2 L10 5" stroke="var(--green)" fill="none" stroke-width="1.4"/></svg>Pre - purchase inspections</li>
</ul>
<ul class="abs ticks" style="left:385px;top:2798px">
  <li><svg class="tick" viewBox="0 0 14 14"><circle cx="7" cy="7" r="6" stroke="var(--green)" fill="none"/><path d="M4 7 L6.2 9.2 L10 5" stroke="var(--green)" fill="none" stroke-width="1.4"/></svg>Spider</li>
  <li><svg class="tick" viewBox="0 0 14 14"><circle cx="7" cy="7" r="6" stroke="var(--green)" fill="none"/><path d="M4 7 L6.2 9.2 L10 5" stroke="var(--green)" fill="none" stroke-width="1.4"/></svg>Cockroach &amp; Termite</li>
  <li><svg class="tick" viewBox="0 0 14 14"><circle cx="7" cy="7" r="6" stroke="var(--green)" fill="none"/><path d="M4 7 L6.2 9.2 L10 5" stroke="var(--green)" fill="none" stroke-width="1.4"/></svg>Termite Inspections</li>
  <li><svg class="tick" viewBox="0 0 14 14"><circle cx="7" cy="7" r="6" stroke="var(--green)" fill="none"/><path d="M4 7 L6.2 9.2 L10 5" stroke="var(--green)" fill="none" stroke-width="1.4"/></svg>Termite treatments</li>
</ul>
<a class="btn" style="left:199px;top:2928px;width:112px;height:31px">Learn More</a>
<div class="photo" role="img" aria-label="Smiling pest technician with sprayer giving thumbs up" style="left:613px;top:2644px;width:390px;height:325px;background:linear-gradient(240deg,#e8edf0,#b9c4cc 40%,#3b5d8a 70%,#e2d4c7)"></div>
<div class="badge" style="left:583px;top:2775px" aria-hidden="true">
  <svg width="20" height="26" viewBox="0 0 20 26"><path d="M2 1h16v24H2z M5 5h3v3H5z M12 5h3v3h-3z M5 11h3v3H5z M12 11h3v3h-3z M5 17h3v3H5z M12 17h3v3h-3z" fill="var(--white)" fill-rule="evenodd"/></svg>
</div>

<!-- testimonials -->
<svg class="abs" style="left:0;top:3030px" width="1200" height="570" viewBox="0 0 1200 570" preserveAspectRatio="none" role="img" aria-label="Green tinted background photo of a happy customer">
  <path d="M0 70 L1200 0 L1200 570 L0 570Z" fill="var(--green)"/>
  <path d="M0 70 L1200 0 L1200 570 L0 570Z" fill="#2d8a12" opacity=".35"/>
</svg>
<div class="abs" style="left:0;width:1200px;top:3132px;text-align:center;color:var(--white);font-size:33px;font-weight:400">What Our Customers Say</div>
<div class="abs" style="left:548px;top:3188px;width:110px;height:1px;background:var(--white);opacity:.8"></div>

<div class="tcard" style="left:256px;top:3228px"><div class="quote">”</div><p>Sed ut perspiciatis unde omnis iste natus error sit voluptatem accntium doloremque laudantium, totam rem aperiam, eaque ipsa quae ab illo intore veritatis et quasi architecto beatae vitae dicta sunt explicabo. Nemo enim ipsam voluptatem</p><div class="stars">★★★★★</div></div>
<div class="tail" style="left:298px;top:3417px;border-left:40px solid var(--white);border-bottom:32px solid transparent"></div>
<div class="avatar" style="left:360px;top:3440px" role="img" aria-label="Customer portrait"></div>
<div class="who" style="left:445px;top:3462px">SAM REYES<br>BRIGHTLINE CO</div>

<div class="tcard" style="left:618px;top:3228px"><div class="quote">”</div><p>Sed ut perspiciatis unde omnis iste natus error sit voluptatem accntium doloremque laudantium, totam rem aperiam, eaque ipsa quae ab illo intore veritatis et quasi architecto beatae vitae dicta sunt explicabo. Nemo enim ipsam voluptatem</p><div class="stars">★★★★★</div></div>
<div class="tail" style="left:871px;top:3417px;border-right:40px solid var(--white);border-bottom:32px solid transparent"></div>
<div class="avatar" style="left:722px;top:3440px" role="img" aria-label="Customer portrait"></div>
<div class="who" style="left:807px;top:3462px">SAM REYES<br>BRIGHTLINE CO</div>
<div class="abs" style="left:578px;top:3522px;display:flex;gap:9px;align-items:center">
  <i style="width:5px;height:5px;border-radius:50%;background:var(--white)"></i><i style="width:5px;height:5px;border-radius:50%;background:var(--white)"></i><i style="width:9px;height:9px;border-radius:50%;border:1.5px solid var(--white)"></i><i style="width:5px;height:5px;border-radius:50%;background:var(--white)"></i><i style="width:5px;height:5px;border-radius:50%;background:var(--white)"></i>
</div>

<!-- contact -->
<div class="abs" role="img" aria-label="Faded photo of a smiling technician" style="left:0;top:3597px;width:520px;height:510px;background:linear-gradient(90deg,#d9dcdd,#eef0f0 60%,rgba(255,255,255,0))"></div>
<div class="contact-card">
  <div class="abs" style="left:43px;top:42px;font-size:22px;font-weight:500">GET IN TOUCH</div>
  <div class="field" style="left:47px;top:92px;width:210px"><label>First Name <sup>*</sup></label><span>Daniel</span></div>
  <div class="field" style="left:297px;top:92px;width:210px"><label>Last Name <sup>*</sup></label><span>Hart</span></div>
  <div class="field" style="left:47px;top:152px;width:210px"><label>Email Address <sup>*</sup></label><span>daniel.hart@mail.com</span></div>
  <div class="field" style="left:297px;top:152px;width:210px"><label>Phone <sup>*</sup></label><span>555-010-2288</span></div>
  <div class="field" style="left:47px;top:214px;width:420px;height:80px"><label>Message</label><span>Hi, do you have a moment to talk abo...</span></div>
  <div class="abs" style="left:462px;top:258px;width:52px;height:52px;border-radius:50%;background:var(--green);display:flex;align-items:center;justify-content:center">
    <svg width="22" height="22" viewBox="0 0 22 22"><path d="M2 10 L20 2 L13 20 L10 12Z" fill="var(--white)"/></svg>
  </div>
</div>

<!-- footer -->
<svg class="abs" style="left:0;top:4040px" width="1200" height="80" viewBox="0 0 1200 80" preserveAspectRatio="none" aria-hidden="true">
  <path d="M0 70 C300 0 900 0 1200 60 L1200 80 L0 80Z" fill="var(--green)"/>
</svg>
<footer class="footer">
  <svg class="abs" style="left:0;top:0" width="1200" height="30" viewBox="0 0 1200 30" preserveAspectRatio="none" aria-hidden="true"><path d="M0 20 C300 -10 900 -10 1200 10 L1200 0 L0 0Z" fill="var(--green)"/></svg>
  <div class="abs" style="left:215px;top:86px;display:flex;align-items:center;gap:12px;color:var(--white);font-size:40px;font-weight:500"><span style="width:22px;height:22px;border-radius:50%;background:var(--white)"></span>Korvale</div>

  <div class="fhead" style="left:488px;top:42px">Have Any Question</div>
  <svg class="abs" style="left:489px;top:76px" width="14" height="14" viewBox="0 0 14 14"><path d="M3 1 L6 4 L4.5 6 C5.5 8 7 9.5 8 9.5 L10 8 L13 11 L11 13 C6 13 1 8 1 3Z" fill="none" stroke="var(--green-bright)" stroke-width="1.2"/></svg>
  <div class="flink" style="left:511px;top:72px">+66 (0) 2410-5530-2</div>
  <svg class="abs" style="left:489px;top:114px" width="14" height="14" viewBox="0 0 14 14"><path d="M7 13 C3 8 3 6 3 5 A4 4 0 0 1 11 5 C11 6 11 8 7 13Z" fill="none" stroke="var(--green-bright)" stroke-width="1.2"/><circle cx="7" cy="5" r="1.4" fill="var(--green-bright)"/></svg>
  <div class="flink" style="left:511px;top:110px;width:210px;line-height:16px">18 Moo 7 Riverside Road,<br>Nong Chok Business Park,<br>Bangkok, 10530 Thailand</div>
  <svg class="abs" style="left:489px;top:188px" width="14" height="14" viewBox="0 0 14 14"><rect x="1" y="3" width="12" height="8" fill="none" stroke="var(--green-bright)" stroke-width="1.2"/><path d="M1 3 L7 8 L13 3" fill="none" stroke="var(--green-bright)" stroke-width="1.2"/></svg>
  <div class="flink" style="left:511px;top:184px">hello@korvalepest.com</div>

  <div class="fhead" style="left:745px;top:42px">Info</div>
  <div class="flink" style="left:745px;top:72px">Home<br>About Us<br>Services<br>Pricing<br>Blog<br>Contact Us</div>

  <div class="fhead" style="left:870px;top:42px">Social</div>
  <div class="social" style="left:874px;top:92px"></div>
  <div class="social" style="left:904px;top:92px"></div>
  <div class="social" style="left:934px;top:92px"></div>

  <div class="abs" style="left:0;top:245px;width:1200px;height:1px;background:#33383b"></div>
  <div class="copy" style="left:216px;top:266px">© 2021 <span style="color:var(--green-bright)">Korvale Pest Solutions</span>. All Rights Reserved.</div>
  <div class="copy" style="left:836px;top:266px">Privacy Policy &nbsp; | &nbsp; Terms of Use</div>
</footer>

</div>
</body>
</html>
```